Brightly Fen business card for handing simple contact information and generating service awareness

Utilizing the attached logo(s), generate a professional, but approachable, card conveying a sense of capability and integrity. Please only use one logo of the four attached; the different colors are all acceptable, but preference will be given to a design integrating a teal/turquoise logo,

I do not know where to put in the contact information or details?

Target Market(s)

Agriculture, Farming, Timber, Forestry, Construction, Crane Service

Industry/Entity Type

Contact Information for Business Card

Name, Phone Number, email address

Colors

Designer to choose colors to be used in the design.

Requirements
Nice to have
• It would be great to have either a mountain or one of the attached cranes as a backdrop on the rear of the card. Simple watermarks and/or Debossing is also great

```html
<!DOCTYPE html>
<html lang="en">
<head>
<meta charset="utf-8">
<title>Brightly Fen — Business Card</title>
<link rel="stylesheet" href="https://fonts.googleapis.com/css2?family=Montserrat:wght@400;500;700;800&display=swap">
<style>
  :root {
    --backdrop: #3b3532;
    --card-white: #f7f7f6;
    --brand-green: #1f6b58;
    --teal-deep: #1f7465;
    --teal-mid: #2b8a78;
    --teal-light: #3fa690;
    --ink: #2b2b2b;
    --watermark: #ececeb;
  }
  * { box-sizing: border-box; margin: 0; padding: 0; }
  html, body {
    width: 1200px; height: 716px; overflow: hidden;
    background: var(--backdrop);
    font-family: "Montserrat", sans-serif;
  }
  .stage {
    position: relative; width: 1200px; height: 716px;
  }
  .card {
    position: absolute; top: 209px;
    width: 520px; height: 297px;
    border-radius: 3px; overflow: hidden;
    box-shadow: 0 10px 28px rgba(0,0,0,.35);
  }

  /* Back side */
  .card-back {
    left: 60px;
    background: linear-gradient(135deg, var(--teal-deep) 0%, var(--teal-mid) 65%, var(--teal-light) 100%);
  }
  .back-pattern {
    position: absolute; inset: 0;
    background: linear-gradient(135deg, rgba(0,0,0,.06), rgba(255,255,255,.07));
  }
  .back-brand {
    position: absolute; right: 34px; bottom: 34px;
    display: flex; align-items: center; gap: 7px;
  }
  .back-brand .brand-dot {
    width: 14px; height: 14px; border-radius: 50%; background: #ffffff;
  }
  .back-brand .brand-name {
    color: #ffffff; font-weight: 800; font-size: 15px; letter-spacing: .04em;
  }

  /* Front side */
  .card-front {
    left: 620px;
    background: var(--card-white);
  }
  .front-watermark {
    position: absolute; right: -40px; bottom: -60px;
    width: 300px; height: 300px; border-radius: 50%;
    background: radial-gradient(circle at 50% 50%, var(--watermark) 0%, rgba(236,236,235,0) 72%);
  }
  .front-brand {
    position: absolute; left: 44px; top: 30px;
    display: flex; align-items: center; gap: 10px;
  }
  .front-brand .brand-dot {
    width: 30px; height: 30px; border-radius: 50%; background: var(--brand-green);
  }
  .front-brand .brand-name {
    color: var(--brand-green); font-weight: 800; font-size: 24px; letter-spacing: .03em;
  }
  .name-marker {
    position: absolute; left: 0; top: 96px;
    width: 12px; height: 34px; background: var(--brand-green);
  }
  .person {
    position: absolute; left: 30px; top: 94px;
  }
  .person-name {
    color: var(--brand-green); font-weight: 800; font-size: 22px; letter-spacing: .03em; line-height: 1.1;
  }
  .person-role {
    color: var(--ink); font-weight: 400; font-size: 14px; margin-top: 3px;
  }
  .contact-list {
    position: absolute; left: 30px; top: 166px;
    list-style: none;
  }
  .contact-list li {
    display: flex; align-items: center; gap: 8px;
    color: var(--ink); font-size: 14px; font-weight: 400;
    height: 25px;
  }
  .contact-list svg { width: 13px; height: 13px; fill: var(--brand-green); flex: none; }
</style>
</head>
<body>
<main class="stage">

  <section class="card card-back" aria-label="Business card, back">
    <div class="back-pattern" role="img" aria-label="Debossed repeating pattern of the company emblem across the teal card"></div>
    <div class="back-brand">
      <span class="brand-dot"></span>
      <span class="brand-name">BRIGHTLY FEN</span>
    </div>
  </section>

  <section class="card card-front" aria-label="Business card, front">
    <div class="front-watermark" role="img" aria-label="Faint watermark of mountain, pine trees and tractor"></div>

    <div class="front-brand">
      <span class="brand-dot"></span>
      <span class="brand-name">BRIGHTLY FEN</span>
    </div>

    <span class="name-marker"></span>
    <div class="person">
      <p class="person-name">DALE WHITFORD</p>
      <p class="person-role">CEO/Founder</p>
    </div>

    <ul class="contact-list">
      <li>
        <svg viewBox="0 0 24 24" aria-hidden="true"><path d="M6.6 10.8a15.1 15.1 0 0 0 6.6 6.6l2.2-2.2c.3-.3.7-.4 1-.2 1.1.4 2.3.6 3.6.6.6 0 1 .4 1 1V20c0 .6-.4 1-1 1A17 17 0 0 1 3 4c0-.6.4-1 1-1h3.5c.6 0 1 .4 1 1 0 1.3.2 2.5.6 3.6.1.3 0 .7-.2 1z"/></svg>
        123-480-61572
      </li>
      <li>
        <svg viewBox="0 0 24 24" aria-hidden="true"><path d="M7 1h10a2 2 0 0 1 2 2v18a2 2 0 0 1-2 2H7a2 2 0 0 1-2-2V3a2 2 0 0 1 2-2zm0 3v14h10V4zm5 15.5a1 1 0 1 0 0 2 1 1 0 0 0 0-2z"/></svg>
        126-480-39158
      </li>
      <li>
        <svg viewBox="0 0 24 24" aria-hidden="true"><path d="M2 5h20v14H2zm2 2v.5l8 5 8-5V7zm0 2.8V17h16V9.8l-8 5z"/></svg>
        info@brightlyfentt.com
      </li>
      <li>
        <svg viewBox="0 0 24 24" aria-hidden="true"><path d="M12 2a10 10 0 1 0 0 20 10 10 0 0 0 0-20zm6.9 6h-3a15 15 0 0 0-1.3-4A8 8 0 0 1 18.9 8zM12 4c.8 1.2 1.5 2.5 1.9 4h-3.8c.4-1.5 1.1-2.8 1.9-4zM4.3 14a8 8 0 0 1 0-4h3.4a16 16 0 0 0 0 4zm.8 2h3a15 15 0 0 0 1.3 4A8 8 0 0 1 5.1 16zm3-8h-3a8 8 0 0 1 4.3-4A15 15 0 0 0 8.1 8zM12 20c-.8-1.2-1.5-2.5-1.9-4h3.8c-.4 1.5-1.1 2.8-1.9 4zm2.3-6H9.7a14 14 0 0 1 0-4h4.6a14 14 0 0 1 0 4zm.3 6a15 15 0 0 0 1.3-4h3a8 8 0 0 1-4.3 4zm1.7-6a16 16 0 0 0 0-4h3.4a8 8 0 0 1 0 4z"/></svg>
        www.brightlyfentt.com
      </li>
    </ul>
  </section>

</main>
</body>
</html>
```